Manufacturing company needs new business card.

I need a unique Business Card that will truly stand out. Nothing too busy. Simple is good, right? Not looking for a standard design either. No cookie cutter layout. I am just looking for something interesting and a bit different. Does't have to completely off the wall crazy, just not your run of the mill business card. Clean and modern with a touch of industrial.

Target Market(s)

Air conditioning industry, Architects, builders.

Industry/Entity Type

Business

Contact Information for Business Card

Details to be included on card are:

Peter Walsh
Managing Director

T: 1300 418 592
M: 0427 385 914
W: www.brandvalefabrication.com.au
E: peter.walsh@brandvalefabrication.com.au
A: 58 Harlow Lane, Sydney NSW 2000

Font styles to use
Sans Serif

Colors
0355a3
848484
fbfbfb

Requirements
Must have
• Card design must be landscape.

```html
<!DOCTYPE html>
<html lang="en">
<head>
<meta charset="utf-8">
<title>Brandvale Fabrication – Business Card</title>
<link rel="stylesheet" href="https://fonts.googleapis.com/css2?family=Roboto:wght@300;400;500&display=swap">
<style>
  :root {
    --brand-blue: #1f4fa3;
    --ink-blue: #2a52b0;
    --steel-grey: #848484;
    --paper: #fbfbfb;
    --backdrop: #2a2a2a;
    --rule: #c4c4c4;
  }
  * { box-sizing: border-box; margin: 0; padding: 0; }
  html, body {
    width: 1200px; height: 900px; overflow: hidden;
    background: var(--backdrop);
    font-family: "Roboto", Arial, sans-serif;
  }
  .sheet {
    width: 1200px; height: 900px;
    display: flex; flex-direction: column;
    align-items: center; justify-content: center; gap: 40px;
  }
  .card {
    width: 700px; height: 400px;
    border-radius: 24px;
    position: relative;
    overflow: hidden;
  }

  /* Front */
  .card--front { background: var(--brand-blue); }
  .front-brand {
    position: absolute; left: 300px; top: 250px;
    display: flex; align-items: center; gap: 16px;
  }
  .front-brand__square {
    width: 26px; height: 26px; background: var(--paper);
  }
  .front-brand__name {
    color: var(--paper); font-weight: 400; font-size: 30px; letter-spacing: 0.2px;
    line-height: 1.1;
  }

  /* Back */
  .card--back { background: var(--paper); }
  .back-row {
    position: absolute; left: 40px; right: 24px; top: 200px;
    display: flex; align-items: center;
  }
  .back-brand {
    width: 140px; color: var(--brand-blue);
    font-weight: 500; font-size: 17px; line-height: 1.25;
  }
  .divider {
    width: 1px; height: 110px; background: var(--rule); margin: 0 14px;
  }
  .person { width: 170px; }
  .person__name {
    color: var(--ink-blue); font-size: 20px; font-weight: 400; letter-spacing: 0.3px;
  }
  .person__role {
    color: var(--steel-grey); font-size: 14px; margin-top: 2px;
    padding-bottom: 8px; border-bottom: 1px solid var(--steel-grey);
  }
  .person__address {
    color: var(--ink-blue); font-size: 14px; line-height: 1.35; margin-top: 8px;
  }
  .contacts { list-style: none; }
  .contacts li {
    display: flex; align-items: center; gap: 8px;
    color: var(--ink-blue); font-size: 13.5px; line-height: 1.75;
    white-space: nowrap;
  }
  .contacts svg { width: 12px; height: 12px; flex: none; fill: var(--steel-grey); }
</style>
</head>
<body>
<main class="sheet">
  <section class="card card--front" aria-label="Card front">
    <div class="front-brand">
      <span class="front-brand__square"></span>
      <span class="front-brand__name">Brandvale Fabrication<br>Australia</span>
    </div>
  </section>

  <section class="card card--back" aria-label="Card back">
    <div class="back-row">
      <div class="back-brand">Brandvale<br>Fabrication</div>
      <span class="divider"></span>
      <div class="person">
        <p class="person__name">PETER WALSH</p>
        <p class="person__role">Managing Director</p>
        <p class="person__address">58 Harlow Lane<br>Sydney NSW 2000</p>
      </div>
      <span class="divider"></span>
      <ul class="contacts">
        <li>
          <svg viewBox="0 0 12 12" aria-hidden="true"><path d="M2.5 0.8 4.3 2.6 3.4 4.2c.8 1.8 2.2 3.2 4 4l1.6-.9 1.8 1.8-1 1.9C5.2 10.7 1.3 6.8 1 2.2z"/></svg>
          1300 418 592
        </li>
        <li>
          <svg viewBox="0 0 12 12" aria-hidden="true"><path d="M3.5 0.5h5a1 1 0 0 1 1 1v9a1 1 0 0 1-1 1h-5a1 1 0 0 1-1-1v-9a1 1 0 0 1 1-1zm.3 1.5v6.8h4.4V2z"/></svg>
          0427 385 914
        </li>
        <li>
          <svg viewBox="0 0 12 12" aria-hidden="true"><path d="M1 2.5h10v7H1zm1.2 1 3.8 3 3.8-3v-.1H2.2zm-.2 1.2v4h8v-4L6 7.8z"/></svg>
          peter.walsh@brandvalefabrication.com.au
        </li>
        <li>
          <svg viewBox="0 0 12 12" aria-hidden="true"><path d="M6 .8a5.2 5.2 0 1 0 0 10.4A5.2 5.2 0 0 0 6 .8zm0 1c.6.6 1.1 1.8 1.2 3.6H4.8C4.9 3.6 5.4 2.4 6 1.8zm-1.2 4.6h2.4c-.1 1.8-.6 3-1.2 3.6-.6-.6-1.1-1.8-1.2-3.6zM1.9 5.4a4.2 4.2 0 0 1 2.2-3.1c-.3.8-.5 1.9-.6 3.1zm0 1.2h1.6c.1 1.2.3 2.3.6 3.1a4.2 4.2 0 0 1-2.2-3.1zm6.6 0h1.6a4.2 4.2 0 0 1-2.2 3.1c.3-.8.5-1.9.6-3.1zm0-1.2c-.1-1.2-.3-2.3-.6-3.1a4.2 4.2 0 0 1 2.2 3.1z"/></svg>
          www.brandvalefabrication.com.au
        </li>
      </ul>
    </div>
  </section>
</main>
</body>
</html>
```